Bref créative
Bellquist law p.a.
See logo attached
Simple
Hal Bellquist
Board Certified Trial Lawyer
Post Office Box 48716
27 West Caldera Street
Marlowe Bay, Georgia. 30874
Hal@bellquistlegal.example
Www.halbellquist.example
Here is a version with a slight varation in the size of bellquist law
Here is the final version of the logo with the bellquist law text included with the font that I though was most suitable. There is a white outline on this version that is not on the final version. It is a tif file that will not upload to this server but is on my facebook page. I can email it privately if someone needs it. I think this logo may look better on grey paper. The black background that I have in this attachment may not be feasible since it would require three colors on the letterhead. Anyway, thanks for your help.

```html
<!DOCTYPE html>
<html lang="en">
<head>
<meta charset="utf-8">
<title>Bellquist Law, P. A. — Stationery</title>
<link rel="stylesheet" href="https://fonts.googleapis.com/css2?family=Didact+Gothic&display=swap">
<style>
  :root {
    --orange: #ee6b21;
    --ink: #4a4a4a;
    --muted: #7a7a7a;
    --paper: #ffffff;
    --edge: #d9d9d9;
    --backdrop: #ffffff;
  }
  * { box-sizing: border-box; margin: 0; padding: 0; }
  html, body {
    width: 1200px; height: 1101px; overflow: hidden;
    background: var(--backdrop);
    font-family: "Didact Gothic", "Century Gothic", sans-serif;
    color: var(--ink);
  }
  .stationery { position: relative; width: 1200px; height: 1101px; }

  .sheet {
    position: absolute; background: var(--paper);
    border: 1px solid var(--edge);
    box-shadow: 2px 3px 6px rgba(0,0,0,.12);
  }

  /* Brand lockup: name set as text, plain circle beside it */
  .brand { display: flex; align-items: center; justify-content: center; gap: 7px; color: var(--orange); white-space: nowrap; }
  .brand-dot { border-radius: 50%; background: var(--orange); flex: none; }

  /* Letterhead */
  .letterhead { left: 54px; top: 84px; width: 720px; height: 987px; }
  .letterhead .brand { position: absolute; left: 0; right: 0; top: 150px; font-size: 16px; }
  .letterhead .brand-dot { width: 10px; height: 10px; }
  .letterhead-footer {
    position: absolute; left: 0; right: 0; bottom: 22px;
    text-align: center; font-size: 10.5px; line-height: 15px; color: var(--ink);
  }
  .letterhead-footer .accent { color: var(--orange); }
  .letterhead-band { position: absolute; left: 0; right: 0; bottom: 0; height: 10px; background: var(--orange); }

  /* Business card */
  .card { left: 834px; top: 216px; width: 330px; height: 159px; }
  .card .brand { position: absolute; right: 24px; top: 62px; font-size: 9px; gap: 4px; }
  .card .brand-dot { width: 6px; height: 6px; }
  .card-name { position: absolute; left: 12px; top: 12px; font-size: 10px; color: var(--orange); }
  .card-title { position: absolute; left: 12px; top: 25px; font-size: 6px; color: var(--muted); }
  .card-contact {
    position: absolute; left: 66px; right: 8px; top: 92px;
    font-size: 6px; line-height: 9px; color: var(--muted);
  }

  /* Envelope */
  .envelope { left: 504px; top: 675px; width: 666px; height: 345px; overflow: hidden; }
  .envelope-flap { position: absolute; left: 0; top: 0; width: 666px; height: 112px; }
  .envelope .brand { position: absolute; left: 0; right: 0; top: 200px; font-size: 14px; }
  .envelope .brand-dot { width: 9px; height: 9px; }
  .envelope-address {
    position: absolute; left: 0; right: 0; bottom: 88px;
    text-align: center; font-size: 10px; color: var(--ink);
  }
</style>
</head>
<body>
<main class="stationery">

  <section class="sheet letterhead" aria-label="Letterhead">
    <div class="brand"><span class="brand-dot"></span><span>Bellquist Law, P. A.</span></div>
    <footer class="letterhead-footer">
      <p>Post Office Box 48716 &nbsp;27 West Caldera Street Marlowe Bay, Georgia. 30874 &nbsp;<span class="accent">P</span> 4785550142</p>
      <p><span class="accent">F</span> 4785550187 &nbsp;|&nbsp; 8665550139 &nbsp;|&nbsp; hal@bellquistlegal.example &nbsp;<span class="accent">www.halbellquist.example</span></p>
    </footer>
    <div class="letterhead-band"></div>
  </section>

  <section class="sheet card" aria-label="Business card">
    <p class="card-name">Hal Bellquist</p>
    <p class="card-title">Board Certified Trial Lawyer</p>
    <div class="brand"><span class="brand-dot"></span><span>Bellquist Law, P. A.</span></div>
    <div class="card-contact">
      <p>Post Office Box 48716 | 27 West Caldera Street Marlowe Bay,</p>
      <p>Georgia. 30874 | P 4785550142 | F 4785550187 | 8665550139</p>
      <p>hal@bellquistlegal.example | www.halbellquist.example</p>
    </div>
  </section>

  <section class="sheet envelope" aria-label="Envelope">
    <svg class="envelope-flap" viewBox="0 0 666 112" aria-hidden="true">
      <polygon points="0,0 666,0 666,12 370,104 333,112 296,104 0,12" fill="var(--orange)"/>
    </svg>
    <div class="brand"><span class="brand-dot"></span><span>Bellquist Law, P. A.</span></div>
    <p class="envelope-address">Post Office Box 48716 &nbsp;27 West Caldera Street Marlowe Bay, Georgia. 30874</p>
  </section>

</main>
</body>
</html>
```